eBook Brochure - How to ebook on digital marketing

I would like to have this Marketing ebook laid out to look professional, yet fun & cool... easy to read... similar to eBooks that you can download from Plumvane.com or similar sites.

I have provided the copy and some graphic inspiration within it as well as a sample e-book I have attached to provide an example of what I like (but not to copy exactly, but I do like the layout... so something similar to it). I would like a modern, simple, clean look with easy to read graphic icons representing different elements randomly throughout.

Target Market(s)

Small to medium sized businesses interested in marketing

Industry/Entity Type

Digital

Font styles to use
Sans Serif

Requirements
Must have
• Clean professional look with graphic icons, social media icons, header and or footer some consistent look to the e-book. It will be in a printable downloadable PDF file sent to potential customers ... easy to read
Nice to have
• graphic icons, I like dots, white space
Should not have
• Too busy

```html
<!DOCTYPE html>
<html lang="en">
<head>
<meta charset="utf-8">
<title>10 Essential Tools &amp; Tips to Generate Leads Today</title>
<link href="https://fonts.googleapis.com/css2?family=Open+Sans:wght@400;600;700;800&family=Oswald:wght@500;700&display=swap" rel="stylesheet">
<style>
:root{
  --teal:#3a9d94;
  --teal-light:#d9efec;
  --ink:#4a4a4a;
  --muted:#8a8a8a;
  --paper:#ffffff;
  --stage:#e9e6e1;
}
*{box-sizing:border-box;margin:0;padding:0}
html,body{width:880px;height:1200px;overflow:hidden}
body{background:var(--stage);position:relative;font-family:"Open Sans",Arial,sans-serif;color:var(--ink)}
.page{position:absolute;width:290px;height:380px;background:var(--paper);box-shadow:0 2px 6px rgba(0,0,0,.18);padding:18px 20px 0;overflow:hidden}
.col-left{left:130px}.col-right{left:460px}
.row-1{top:15px}.row-2{top:410px}.row-3{top:805px}
p{font-size:5.2px;line-height:1.55;margin-bottom:5px;color:var(--ink)}
.section-title{font-size:6.3px;font-weight:700;color:var(--teal);margin:6px 0 2px;display:flex;align-items:center;gap:4px}
.section-title::before{content:"";width:4px;height:4px;background:var(--teal);flex:none}
.page-footer{position:absolute;left:0;right:0;bottom:0;height:22px;border-top:1px solid var(--teal-light);display:flex;align-items:center;justify-content:space-between;padding:0 20px}
.page-number{width:12px;height:12px;background:var(--teal);color:#fff;font-size:6px;font-weight:700;display:flex;align-items:center;justify-content:center}
.brand{display:flex;align-items:center;gap:3px;font-size:6px;font-weight:700;color:var(--teal)}
.brand-dot{width:6px;height:6px;border-radius:50%;background:var(--teal)}
.url{font-size:5px;color:var(--muted)}
/* back cover */
.about-title{font-size:17px;font-weight:700;color:var(--teal);margin-bottom:6px}
.talk{display:flex;gap:12px;margin-top:10px}
.portrait{width:78px;height:92px;background:linear-gradient(160deg,#c9ccd0,#7d858d)}
.talk-text{flex:1;text-align:right;padding-top:16px}
.talk-title{font-size:15px;font-weight:700;color:var(--teal)}
.talk-sub{font-size:6.5px;font-weight:700;margin:3px 0}
.back-strip{position:absolute;left:0;right:0;bottom:0;height:18px;background:var(--teal);color:#fff;font-size:6px;display:flex;align-items:center;justify-content:center;letter-spacing:.5px}
/* front cover */
.cover{padding:0}
.cover-art{height:170px;background:linear-gradient(180deg,#ffffff 0%,var(--teal-light) 40%,var(--teal) 100%)}
.cover-brand{display:flex;align-items:center;gap:5px;margin:14px 0 0 26px;font-size:9px;font-weight:700;color:var(--teal)}
.cover-brand .brand-dot{width:10px;height:10px}
.cover-title{font-family:"Oswald",Arial,sans-serif;font-weight:700;font-size:46px;line-height:1;color:var(--teal);text-align:center;margin-top:22px;letter-spacing:.5px}
.cover-sub{font-size:8.2px;font-weight:700;text-align:center;letter-spacing:.6px;margin-top:6px;color:var(--ink)}
.cover-rule{width:200px;height:1px;background:var(--teal);margin:10px auto 0}
.cover .page-footer{justify-content:center}
/* chapter header */
.chapter{display:flex;align-items:flex-end;gap:6px;border-bottom:2px solid var(--teal);padding-bottom:4px;margin-bottom:8px}
.chapter-num{font-family:"Oswald",Arial,sans-serif;font-size:30px;font-weight:700;color:var(--teal);line-height:.9}
.chapter-name{font-family:"Oswald",Arial,sans-serif;font-size:17px;font-weight:500;color:var(--ink);line-height:1}
.chapter-name.small{font-size:12px}
.photo-people{height:140px;margin-top:8px;background:linear-gradient(180deg,#eef1f3,#9aa3ab)}
.photo-laptop{width:110px;height:60px;margin:6px auto 0;background:linear-gradient(180deg,#dfe3e6,#8f979e)}
.topic-list{list-style:none;columns:2;font-size:5.2px;line-height:1.7;margin:2px 0 0 8px}
.topic-list li::before{content:"• ";color:var(--teal)}
</style>
</head>
<body>

<section class="page col-left row-1">
  <h2 class="about-title">About Us</h2>
  <p>We help small and growing businesses turn online visitors into loyal customers through smart, simple and measurable digital marketing plans.</p>
  <p>Our team blends design, content and data to build campaigns that feel personal, look sharp and deliver steady results month after month.</p>
  <p>From websites to social media, we focus on the tools that matter most and skip the noise that wastes your time and budget.</p>
  <p>This guide shares the ten ideas we use every day. Try one, try them all, and watch your pipeline grow.</p>
  <div class="talk">
    <div class="portrait" role="img" aria-label="Portrait photo of the agency contact"></div>
    <div class="talk-text">
      <div class="talk-title">Let's Talk!</div>
      <div class="talk-sub">Thanks for stopping by!</div>
      <p>We'd love to hear about your goals. Reach out anytime.</p>
    </div>
  </div>
  <div class="back-strip">www.northpeakmedia.com</div>
</section>

<section class="page cover col-right row-1">
  <div class="cover-art" role="img" aria-label="Illustration of a computer monitor growing a tree of marketing icons"></div>
  <div class="cover-brand"><span class="brand-dot"></span>Northpeak Media</div>
  <h1 class="cover-title">10 ESSENTIAL</h1>
  <div class="cover-sub">TOOLS &amp; TIPS TO GENERATE LEADS TODAY</div>
  <div class="cover-rule"></div>
  <div class="page-footer"><span class="url">www.northpeakmedia.com</span></div>
</section>

<section class="page col-left row-2">
  <div class="chapter"><span class="chapter-num">#1</span><span class="chapter-name">WEBSITE</span></div>
  <p>Your website is the heart of every campaign. Make it easy to find, fast to load and clear about what you offer.</p>
  <h3 class="section-title">Keep It Simple</h3>
  <p>Use short pages, plenty of white space and one clear goal per page so visitors never feel lost.</p>
  <h3 class="section-title">Add Calls to Action</h3>
  <p>Place bold buttons where eyes land first and invite people to download, call or sign up.</p>
  <h3 class="section-title">Optimize for Search</h3>
  <p>Write titles and headings around the words your buyers type, and refresh older pages often.</p>
  <h3 class="section-title">Go Mobile First</h3>
  <p>Most visitors arrive on a phone, so test every page on small screens before you publish.</p>
  <h3 class="section-title">Track Everything</h3>
  <p>Set up simple analytics to learn which pages bring leads and which need work.</p>
  <div class="page-footer"><span class="page-number">1</span><span class="brand"><span class="brand-dot"></span>Northpeak Media</span></div>
</section>

<section class="page col-right row-2">
  <h3 class="section-title">Landing Pages That Convert</h3>
  <p>Match each ad or email to its own page with one offer and a short form.</p>
  <h3 class="section-title">Speed Matters</h3>
  <p>Compress images and trim scripts so pages open in under three seconds.</p>
  <h3 class="section-title">Social Proof</h3>
  <p>Share reviews, client logos and short stories that show real results from real people.</p>
  <h3 class="section-title">Clear Contact Details</h3>
  <p>Show your phone and email on every page so ready buyers can reach you at once.</p>
  <div class="photo-people" role="img" aria-label="Photo of two smiling business people in suits"></div>
  <div class="page-footer"><span class="brand"><span class="brand-dot"></span>Northpeak Media</span><span class="page-number">2</span></div>
</section>

<section class="page col-left row-3">
  <div class="chapter"><span class="chapter-num">#2</span><span class="chapter-name small">BLOGGING/<br>ARTICLE MARKETING</span></div>
  <p>Fresh articles give search engines a reason to visit and give readers a reason to trust you.</p>
  <h3 class="section-title">Publish Often</h3>
  <p>A steady schedule builds habit. Aim for one helpful post each week.</p>
  <h3 class="section-title">Solve Real Problems</h3>
  <p>Answer the questions customers ask most and link to a useful next step.</p>
  <h3 class="section-title">Topics to Try</h3>
  <ul class="topic-list">
    <li>How-to guides</li><li>Industry news</li><li>Case studies</li>
    <li>Expert interviews</li><li>Checklists</li><li>Myth busters</li>
  </ul>
  <div class="photo-laptop" role="img" aria-label="Illustration of a laptop showing a blog page"></div>
  <div class="page-footer"><span class="page-number">3</span><span class="brand"><span class="brand-dot"></span>Northpeak Media</span></div>
</section>

<section class="page col-right row-3">
  <div class="chapter"><span class="chapter-num">#3</span><span class="chapter-name">Public Relations</span></div>
  <p>Good press puts your name in front of new audiences and lends instant credibility.</p>
  <h3 class="section-title">Write a PR Strategy</h3>
  <p>Decide who you want to reach, which outlets they read and what story you will tell.</p>
  <h3 class="section-title">Build Relationships</h3>
  <p>Follow local reporters, share their work and pitch only when your news truly fits.</p>
  <h3 class="section-title">Share Your Wins</h3>
  <p>Awards, new hires and big projects all make simple, timely releases.</p>
  <h3 class="section-title">Use Press Kits</h3>
  <p>Keep a page with photos, facts and contacts ready for writers on deadline.</p>
  <h3 class="section-title">Measure Coverage</h3>
  <p>Note every mention and the traffic it brings to learn what works.</p>
  <div class="page-footer"><span class="brand"><span class="brand-dot"></span>Northpeak Media</span><span class="page-number">4</span></div>
</section>

</body>
</html>
```